Company Website

Our company teaches Federal Accredited EMT certification. Our company name is Corvane Training Group. (logo is in the files). We have a current website that needs an overhaul (www.corvanetraininggroup.com). This website needs to able to be used on wordpress. We need a website that has a good flow and design, have a page that has our instructor bio’s, a page on our class information, prerequisites, and how many seats are left in the class, a page that will accept payments and layout our cost. Be able to expand as our company expands to other classes (CPR ETC.)

Target Market(s)

People that want to take an EMT class

Coding

Coded - Design and coding required

Number of Pages Required

3 page

Requirements
Must have
• A page explaining who we are, a page of the services we offer with the ability to pay using Quidora or some external source, and a page about who the instructors are.
Nice to have
• Good flow, easy to change as the Business grows

```html
<!DOCTYPE html>
<html lang="en">
<head>
<meta charset="utf-8">
<title>Corvane Training Group</title>
<link href="https://fonts.googleapis.com/css2?family=Montserrat:wght@400;500;600;700&family=Open+Sans:wght@400;600&display=swap" rel="stylesheet">
<style>
:root{
  --navy:#1b232d;
  --navy-2:#232d38;
  --red:#e8193c;
  --white:#ffffff;
  --grey-bg:#e9e9e9;
  --card-bg:#e6e6e6;
  --text:#333a42;
  --muted:#9aa3ad;
  --footer:#0c0e11;
}
*{box-sizing:border-box;margin:0;padding:0}
html,body{width:1200px;height:3826px;overflow:hidden}
body{position:relative;background:var(--white);font-family:'Montserrat',sans-serif;color:var(--text)}
.abs{position:absolute}

/* header */
.site-header{left:0;top:0;width:1200px;height:97px;background:var(--navy)}
.brand{left:143px;top:20px;display:flex;align-items:center;gap:10px}
.brand-mark{width:26px;height:26px;border-radius:50%;background:var(--red)}
.brand-name{font-family:'Montserrat',sans-serif;font-weight:600;font-size:21px;color:var(--white);letter-spacing:.5px}
.contact-line{right:144px;top:20px;font-size:15px;color:var(--white);display:flex;align-items:center;gap:6px}
.contact-line b{font-weight:700}
.main-nav{right:144px;top:62px;display:flex;gap:33px;font-size:12px;font-weight:500;color:var(--white)}
.main-nav .active{position:relative}
.main-nav .active::after{content:"";position:absolute;left:-2px;right:-2px;top:20px;height:7px;background:var(--red)}

/* hero */
.hero{left:0;top:97px;width:1200px;height:593px}
.hero-text{left:0;top:130px;width:1200px;text-align:center;color:var(--white)}
.hero-title{font-size:50px;font-weight:700;letter-spacing:.5px}
.hero-copy{margin:16px auto 0;width:800px;font-size:20px;line-height:37px}
.btn-outline{display:inline-block;margin-top:20px;width:263px;height:54px;line-height:52px;border:2px solid var(--white);font-size:19px;font-weight:600;color:var(--white)}
.hero-arrow{top:335px;width:24px;height:36px}

/* intro */
.section-title{font-weight:600;color:var(--red);text-align:center}
.intro-title{left:0;top:766px;width:1200px;font-size:33px}
.intro-copy{left:140px;top:815px;width:920px;text-align:center;font-size:17px;line-height:32px;color:#333}
.btn-dark{left:539px;top:990px;width:120px;height:39px;background:var(--navy);color:var(--white);font-size:16px;line-height:39px;text-align:center}

/* EMT class */
.emt-panel{left:0;top:1117px;width:600px;height:530px;background:var(--navy)}
.emt-photo{left:600px;top:1133px;width:600px;height:530px;background:radial-gradient(circle at 30% 40%,#c8202e 0%,#5a1a2a 30%,#1c1d33 65%,#0b0d18 100%)}
.emt-title{left:144px;top:1188px;font-size:32px;font-weight:600;color:var(--white)}
.emt-copy{left:144px;top:1246px;font-family:'Open Sans',sans-serif;font-size:13px;line-height:32px;color:#c3cad2}
.emt-copy span{display:block;white-space:nowrap}
.btn-red{background:var(--red);color:var(--white);font-size:16px;text-align:center}
.emt-btn{left:144px;top:1519px;width:119px;height:40px;line-height:40px}

/* countdown */
.countdown{left:0;top:1647px;width:1200px;height:368px;background:var(--grey-bg)}
.timer{left:460px;top:1754px;display:flex;gap:8px}
.timer-box{width:65px;height:80px;border:2px solid var(--navy);text-align:center;padding-top:6px}
.timer-box .num{font-size:42px;font-weight:700;color:var(--navy);line-height:44px}
.timer-box .unit{font-size:10px;color:var(--navy);margin-top:4px}
.until{left:0;top:1846px;width:1200px;text-align:center;font-size:16px;color:#333}
.seats{left:0;top:1864px;width:1200px;text-align:center;font-size:65px;font-weight:700;color:var(--red)}

/* other classes */
.classes-title{left:0;top:2098px;width:1200px;font-size:33px}
.class-card{top:2153px;width:291px;height:384px;background:var(--card-bg)}
.class-card .img{height:193px}
.class-card h3{margin:22px 19px 0;font-size:17px;font-weight:500;line-height:24px;color:#333}
.class-card p{margin:14px 19px 0;font-family:'Open Sans',sans-serif;font-size:10px;line-height:19px;color:#555}
.class-card .btn-red{position:absolute;left:3px;bottom:0;width:119px;height:40px;line-height:40px}
.carousel-arrow{top:2330px;width:20px;height:32px}

/* prerequisite */
.prereq-photo{left:480px;top:2626px;width:720px;height:600px;background:linear-gradient(140deg,#7f8a92 0%,#5d6366 30%,#c9c43a 55%,#d4402c 80%,#3a3f43 100%)}
.prereq-panel{left:0;top:2626px;width:600px;height:600px}
.prereq-title{left:143px;top:2712px;font-size:32px;font-weight:600;color:var(--white)}
.prereq-copy{left:160px;top:2776px;width:330px;font-family:'Open Sans',sans-serif;font-size:10.5px;line-height:24px;color:#a9b2bb}
.prereq-copy p+p{margin-top:24px}
.prereq-bar{left:143px;top:2780px;width:5px;height:348px;background:#8a939b}
.prereq-bar-red{left:143px;top:2780px;width:5px;height:45px;background:var(--red)}

/* contact */
.contact-title{left:0;top:3310px;width:1200px;font-size:33px;line-height:48px}
.contact-item{top:3427px;width:340px;text-align:center;font-size:15px;line-height:24px;color:#333}
.contact-icon{width:80px;height:80px;margin:0 auto 22px;border:1.5px solid #333;border-radius:50%;display:flex;align-items:center;justify-content:center}

/* footer */
.site-footer{left:0;top:3620px;width:1200px;height:206px}
.footer-links{left:143px;top:3733px;font-family:'Open Sans',sans-serif;font-size:11.5px;color:var(--muted);display:flex;gap:12px}
.copyright{left:143px;top:3766px;font-family:'Open Sans',sans-serif;font-size:11.5px;color:var(--muted)}
.social{top:3742px;width:22px;height:22px;border-radius:50%;background:#8d96a0}
.payments{left:832px;top:3735px;width:222px;height:38px;border-radius:19px;background:#242a31;display:flex;align-items:center;justify-content:center;gap:14px}
.pay-card{width:32px;height:20px;border-radius:3px;background:#7e8791}
</style>
</head>
<body>

<header class="abs site-header">
  <div class="abs brand"><span class="brand-mark"></span><span class="brand-name">Corvane Training Group</span></div>
  <div class="abs contact-line">
    <svg width="12" height="12" viewBox="0 0 24 24"><path fill="#fff" d="M6.6 10.8c1.4 2.8 3.8 5.1 6.6 6.6l2.2-2.2c.3-.3.7-.4 1-.2 1.1.4 2.3.6 3.6.6.6 0 1 .4 1 1V20c0 .6-.4 1-1 1C10.6 21 3 13.4 3 4c0-.6.4-1 1-1h3.5c.6 0 1 .4 1 1 0 1.3.2 2.5.6 3.6.1.3 0 .7-.2 1z"/></svg>
    <span><b>555-014-2207</b> – Marcus (Program Director) &nbsp;|&nbsp; <b>555-014-2208</b> – Elena (Owner)</span>
  </div>
  <nav class="abs main-nav">
    <span class="active">HOME</span><span>OUR CLASSES</span><span>PRICING</span><span>REVIEWS</span><span>ABOUT US</span><span>CONTACT US</span>
  </nav>
</header>

<section class="abs hero">
  <svg width="1200" height="593" style="position:absolute;left:0;top:0">
    <defs>
      <radialGradient id="heroGlow" cx="30%" cy="35%" r="80%">
        <stop offset="0" stop-color="#8e1a22"/>
        <stop offset=".45" stop-color="#4b1418"/>
        <stop offset="1" stop-color="#1c1214"/>
      </radialGradient>
    </defs>
    <path d="M0 0H1200V520L600 593L0 520Z" fill="url(#heroGlow)" role="img" aria-label="Ambulance and fire truck at night, lit in red"/>
  </svg>
  <svg class="abs hero-arrow" style="left:52px" viewBox="0 0 24 36"><path d="M18 4L6 18l12 14" stroke="#fff" stroke-width="4" fill="none"/></svg>
  <svg class="abs hero-arrow" style="left:1122px" viewBox="0 0 24 36"><path d="M6 4l12 14L6 32" stroke="#fff" stroke-width="4" fill="none"/></svg>
  <div class="abs hero-text">
    <h1 class="hero-title">YOUR JOURNEY BEGINS</h1>
    <p class="hero-copy">Always find yourself watching the ambulance or fire truck go by and wish you could do that? Do you desire to help the community around you? Let our initial EMT course set you in the career path you desire.</p>
    <span class="btn-outline">Explore Our EMT Class</span>
  </div>
</section>

<h2 class="abs section-title intro-title">Discover In Person Instruction</h2>
<p class="abs intro-copy">At Corvane Training Group the best instruction is done in the classroom. We believe this so much that we only deliver face to face teaching. This allows interaction between the instructor and the student. We teach Federal Accredited EMT, CPR, and continuing education classes for both ALS and BLS providers. Our passion is to give high quality training to those that help others. Here at Corvane Training Group we care about your success. Let us help you in the many different training opportunities available.</p>
<span class="abs btn-dark">Read More</span>

<div class="abs emt-photo" role="img" aria-label="Ambulance with flashing lights at night and a responder walking past"></div>
<section class="abs emt-panel"></section>
<h2 class="abs emt-title">EMT Class</h2>
<p class="abs emt-copy">
  <span>Emergency Medical Technicians or EMTs provide basic emergency</span>
  <span>medical care and transportation for critical and emergent patients</span>
  <span>who access the emergency medical system. This individual pos-</span>
  <span>sess the basic knowledge and skills necessary to provide patient</span>
  <span>care and transportation. Emergency Medical Technicians function</span>
  <span>as part of a comprehensive EMS response, under medical over-</span>
  <span>sight. Emergency Medical Technicians perform interventions with</span>
  <span>the basic equipment typically found on an ambulance.</span>
</p>
<span class="abs btn-red emt-btn">Read More</span>

<section class="abs countdown"></section>
<div class="abs timer">
  <div class="timer-box"><div class="num">14</div><div class="unit">DAYS</div></div>
  <div class="timer-box"><div class="num">23</div><div class="unit">HOURS</div></div>
  <div class="timer-box"><div class="num">32</div><div class="unit">MINUTES</div></div>
  <div class="timer-box"><div class="num">12</div><div class="unit">SECONDS</div></div>
</div>
<div class="abs until">Until</div>
<div class="abs seats">15 Seats Left!!</div>

<h2 class="abs section-title classes-title">Other Classes</h2>
<svg class="abs carousel-arrow" style="left:54px" viewBox="0 0 20 32"><path d="M16 3L4 16l12 13" stroke="#555" stroke-width="3.5" fill="none"/></svg>
<svg class="abs carousel-arrow" style="left:1124px" viewBox="0 0 20 32"><path d="M4 3l12 13L4 29" stroke="#555" stroke-width="3.5" fill="none"/></svg>
<article class="abs class-card" style="left:144px">
  <div class="img" role="img" aria-label="Ambulance speeding at night with motion blur" style="background:linear-gradient(135deg,#1a2035,#b11c25 50%,#2a1a2a)"></div>
  <h3>Nullam accumsan purus vel tempus viverra</h3>
  <p>Mauris suscipit felis id nunc elementum varius. Praesent elementum nulla sit amet justo pellentesque scelerisque.</p>
  <span class="btn-red">Read More</span>
</article>
<article class="abs class-card" style="left:454px">
  <div class="img" role="img" aria-label="Ambulances parked outside a rescue station" style="background:linear-gradient(180deg,#4f7fb8 0%,#9bb3c9 35%,#8b4a3a 60%,#6d6a66 100%)"></div>
  <h3>Vivamus gravida sem a pretium euismod.</h3>
  <p>Mauris suscipit felis id nunc elementum varius. Praesent elementum nulla sit amet justo pellentesque scelerisque.</p>
  <span class="btn-red">Read More</span>
</article>
<article class="abs class-card" style="left:765px">
  <div class="img" role="img" aria-label="Stethoscope resting on a dark surface" style="background:linear-gradient(135deg,#2c2f33,#6b7075 50%,#1a1c1f)"></div>
  <h3>Nam lobortis, purus et fringilla tempus</h3>
  <p>Mauris suscipit felis id nunc elementum varius. Praesent elementum nulla sit amet justo pellentesque scelerisque.</p>
  <span class="btn-red">Read More</span>
</article>

<div class="abs prereq-photo" role="img" aria-label="Yellow and green ambulance on a road"></div>
<svg class="abs prereq-panel" viewBox="0 0 600 600"><path d="M0 0H600L480 588L0 600Z" fill="#232c36" opacity=".96"/><path d="M0 588H482L480 600H0Z" fill="#1b232d"/></svg>
<h2 class="abs prereq-title">Prerequisite</h2>
<div class="abs prereq-bar"></div>
<div class="abs prereq-bar-red"></div>
<div class="abs prereq-copy">
  <p>Vestibulum facilisis dolor at purus tincidunt porta. Nam fringilla nulla vel nisl condimentum, dapibus condimentum enim porta. Phasellus blandit quam a ipsum gravida dapibus. Cras sed augue tortor. Suspendisse elit ligula, iaculis dignissim justo eu, vestibulum venenatis elit. Sed egestas, nisl id cursus ultricies, turpis orci rhoncus odio, id tristique odio ex in lacus.</p>
  <p>Donec quis ex semper, consequat ligula at, efficitur lacus. Phasellus elementum lacinia quam non pellentesque. Aliquam malesuada eros sit amet turpis scelerisque maximus. Maecenas lobortis iaculis efficitur. Nulla facilisi. Vestibulum pharetra diam ex, in posuere purus efficitur ac. Mauris placerat eros lorem, vel egestas mi mattis eget. Donec a nisl vel ante tristique mollis nec quis est. Praesent accumsan nunc a condimentum volutpat. Sed quis metus nibh.</p>
</div>

<h2 class="abs section-title contact-title">If you are interested in joining our class, or<br>have any questions please send us a message.</h2>
<div class="abs contact-item" style="left:105px">
  <div class="contact-icon"><svg width="26" height="34" viewBox="0 0 24 32"><path d="M12 0C5.4 0 0 5.2 0 11.7 0 20 12 32 12 32s12-12 12-20.3C24 5.2 18.6 0 12 0zm0 16a4.5 4.5 0 110-9 4.5 4.5 0 010 9z" fill="#1b232d"/></svg></div>
  Harlow Springs, VA 22190 - USA
</div>
<div class="abs contact-item" style="left:430px">
  <div class="contact-icon"><svg width="32" height="32" viewBox="0 0 24 24"><path fill="#1b232d" d="M6.6 10.8c1.4 2.8 3.8 5.1 6.6 6.6l2.2-2.2c.3-.3.7-.4 1-.2 1.1.4 2.3.6 3.6.6.6 0 1 .4 1 1V20c0 .6-.4 1-1 1C10.6 21 3 13.4 3 4c0-.6.4-1 1-1h3.5c.6 0 1 .4 1 1 0 1.3.2 2.5.6 3.6.1.3 0 .7-.2 1z"/></svg></div>
  555-014-2207 – Marcus (Program Director)<br>555-014-2208 – Elena (Owner)
</div>
<div class="abs contact-item" style="left:755px">
  <div class="contact-icon"><svg width="32" height="24" viewBox="0 0 32 24"><rect width="32" height="24" rx="3" fill="#1b232d"/><path d="M2 3l14 10L30 3" stroke="#fff" stroke-width="2.5" fill="none"/></svg></div>
  hello@corvanetraining.com
</div>

<svg class="abs site-footer" viewBox="0 0 1200 206"><path d="M0 80L600 0L1200 80V206H0Z" fill="var(--footer)"/></svg>
<nav class="abs footer-links"><span>Home</span><span>|</span><span>Our Classes</span><span>|</span><span>Pricing</span><span>|</span><span>Reviews</span><span>|</span><span>About Us</span><span>|</span><span>Contact Us</span></nav>
<div class="abs copyright">Copyright © 2021 &nbsp; Corvane Training Group. &nbsp; All rights reserved.</div>
<span class="abs social" style="left:709px"></span>
<span class="abs social" style="left:772px"></span>
<div class="abs payments"><span class="pay-card"></span><span class="pay-card"></span><span class="pay-card"></span><span class="pay-card"></span></div>

</body>
</html>
```